Image Ads needed for a Pharmacy Education e-commerce website

I need image ads with these specifications:

Supported formats: JPG, PNG, GIF
File size: 3MB max
Recommended aspect ratios: 1:1 square; 4:5 portrait; 4:3 landscape; 16:9 landscape
Recommended resolutions: 1080x1080 square, 1080x1350 portrait, 1440x1080 landscape, 1920x1080 landscape
Thumbnail: Displays at 400x300 pixels
Thumbnail file size: 500KB max

```html
<!DOCTYPE html>
<html lang="en">
<head>
<meta charset="utf-8">
<title>Medora Ad Set – Unlimited Pharmacy CEUs</title>
<link rel="stylesheet" href="https://fonts.googleapis.com/css2?family=Poppins:wght@600&display=swap">
<style>
  :root {
    --stage: #9aa8b5;
    --navy: #003f6b;
    --leaf-green: #6aa11a;
    --ink-light: #ffffff;
    --shadow: 0 6px 14px rgba(20, 35, 55, 0.28);
  }
  * { margin: 0; padding: 0; box-sizing: border-box; }
  html, body { width: 1200px; height: 1029px; overflow: hidden; }
  body {
    background: var(--stage);
    position: relative;
    font-family: "Poppins", sans-serif;
  }
  .ad {
    position: absolute;
    background: var(--navy);
    overflow: hidden;
    box-shadow: var(--shadow);
  }
  .ad-visual {
    position: absolute;
    inset: 0;
    width: 100%;
    height: 100%;
  }
  .visual-arc {
    fill: none;
    stroke: var(--leaf-green);
    stroke-width: 4;
    vector-effect: non-scaling-stroke;
  }
  .offer {
    position: absolute;
    list-style: none;
    color: var(--ink-light);
    font-weight: 600;
    text-transform: uppercase;
  }
  .brand {
    position: absolute;
    display: flex;
    align-items: center;
    color: var(--ink-light);
    font-weight: 600;
    line-height: 1;
  }
  .brand-dot {
    display: inline-block;
    border-radius: 50%;
    background: var(--leaf-green);
  }

  /* 4:5 portrait */
  .ad-portrait { left: 83px; top: 91px; width: 360px; height: 450px; }
  .ad-portrait .offer { left: 30px; top: 62px; font-size: 21px; line-height: 40.5px; }
  .ad-portrait .brand { left: 30px; top: 366px; font-size: 34px; gap: 7px; }
  .ad-portrait .brand-dot { width: 12px; height: 12px; }

  /* 16:9 landscape */
  .ad-wide { left: 477px; top: 91px; width: 640px; height: 360px; }
  .ad-wide .offer { left: 55px; top: 44px; font-size: 30px; line-height: 39px; letter-spacing: 0.12em; }
  .ad-wide .brand { left: 55px; top: 275px; font-size: 28px; gap: 6px; }
  .ad-wide .brand-dot { width: 10px; height: 10px; }

  /* 1:1 square */
  .ad-square { left: 83px; top: 577px; width: 360px; height: 360px; }
  .ad-square .offer { left: 32px; top: 47px; font-size: 19px; line-height: 36.5px; }
  .ad-square .brand { left: 32px; top: 273px; font-size: 30px; gap: 6px; }
  .ad-square .brand-dot { width: 11px; height: 11px; }

  /* 4:3 landscape */
  .ad-standard { left: 477px; top: 488px; width: 480px; height: 360px; }
  .ad-standard .offer { left: 38px; top: 45px; font-size: 22px; line-height: 36.5px; letter-spacing: 0.1em; }
  .ad-standard .brand { left: 38px; top: 273px; font-size: 29px; gap: 6px; }
  .ad-standard .brand-dot { width: 10px; height: 10px; }

  /* 400x300 thumbnail */
  .ad-thumb { left: 983px; top: 488px; width: 133px; height: 100px; }
  .ad-thumb .offer { left: 16px; top: 12px; font-size: 5.5px; line-height: 10.3px; }
  .ad-thumb .brand { left: 16px; top: 75px; font-size: 8px; gap: 2px; }
  .ad-thumb .brand-dot { width: 3px; height: 3px; }
</style>
</head>
<body>

<svg width="0" height="0" style="position:absolute" aria-hidden="true">
  <defs>
    <linearGradient id="photoTone" x1="0" y1="0" x2="1" y2="1">
      <stop offset="0" stop-color="#e9edf3"/>
      <stop offset="0.45" stop-color="#cfd8e3"/>
      <stop offset="1" stop-color="#8796a8"/>
    </linearGradient>
    <radialGradient id="photoGlow" cx="0.42" cy="0.82" r="0.45">
      <stop offset="0" stop-color="#ffd08a" stop-opacity="0.95"/>
      <stop offset="0.4" stop-color="#e0782f" stop-opacity="0.7"/>
      <stop offset="1" stop-color="#e0782f" stop-opacity="0"/>
    </radialGradient>
  </defs>
</svg>

<section class="ad ad-portrait" aria-label="Portrait ad 4:5">
  <svg class="ad-visual" viewBox="0 0 100 100" preserveAspectRatio="none">
    <path role="img" aria-label="Photo: pharmacist looking into a microscope in a lab" d="M68 0 C27.3 20 27.3 80 80 100 L100 100 L100 0 Z" fill="url(#photoTone)"/>
    <path d="M68 0 C27.3 20 27.3 80 80 100 L100 100 L100 0 Z" fill="url(#photoGlow)"/>
    <path class="visual-arc" d="M68 0 C27.3 20 27.3 80 80 100"/>
  </svg>
  <ul class="offer"><li>Unlimited</li><li>PHCE</li><li>CEUs</li><li>$39</li></ul>
  <div class="brand">Medora<span class="brand-dot"></span></div>
</section>

<section class="ad ad-wide" aria-label="Landscape ad 16:9">
  <svg class="ad-visual" viewBox="0 0 100 100" preserveAspectRatio="none">
    <path role="img" aria-label="Photo: pharmacist looking into a microscope in a lab" d="M72 0 C42.3 20 42.3 80 66 100 L100 100 L100 0 Z" fill="url(#photoTone)"/>
    <path d="M72 0 C42.3 20 42.3 80 66 100 L100 100 L100 0 Z" fill="url(#photoGlow)"/>
    <path class="visual-arc" d="M72 0 C42.3 20 42.3 80 66 100"/>
  </svg>
  <ul class="offer"><li>Unlimited</li><li>PHCE</li><li>CEUs</li><li>$39</li></ul>
  <div class="brand">Medora<span class="brand-dot"></span></div>
</section>

<section class="ad ad-square" aria-label="Square ad 1:1">
  <svg class="ad-visual" viewBox="0 0 100 100" preserveAspectRatio="none">
    <path role="img" aria-label="Photo: pharmacist looking into a microscope in a lab" d="M72 0 C24.5 20 24.5 80 69 100 L100 100 L100 0 Z" fill="url(#photoTone)"/>
    <path d="M72 0 C24.5 20 24.5 80 69 100 L100 100 L100 0 Z" fill="url(#photoGlow)"/>
    <path class="visual-arc" d="M72 0 C24.5 20 24.5 80 69 100"/>
  </svg>
  <ul class="offer"><li>Unlimited</li><li>PHCE</li><li>CEUs</li><li>$39</li></ul>
  <div class="brand">Medora<span class="brand-dot"></span></div>
</section>

<section class="ad ad-standard" aria-label="Landscape ad 4:3">
  <svg class="ad-visual" viewBox="0 0 100 100" preserveAspectRatio="none">
    <path role="img" aria-label="Photo: pharmacist looking into a microscope in a lab" d="M72 0 C36.3 20 36.3 80 70 100 L100 100 L100 0 Z" fill="url(#photoTone)"/>
    <path d="M72 0 C36.3 20 36.3 80 70 100 L100 100 L100 0 Z" fill="url(#photoGlow)"/>
    <path class="visual-arc" d="M72 0 C36.3 20 36.3 80 70 100"/>
  </svg>
  <ul class="offer"><li>Unlimited</li><li>PHCE</li><li>CEUs</li><li>$39</li></ul>
  <div class="brand">Medora<span class="brand-dot"></span></div>
</section>

<section class="ad ad-thumb" aria-label="Thumbnail ad 400x300">
  <svg class="ad-visual" viewBox="0 0 100 100" preserveAspectRatio="none">
    <path role="img" aria-label="Photo: pharmacist looking into a microscope in a lab" d="M60 0 C27 20 27 80 65 100 L100 100 L100 0 Z" fill="url(#photoTone)"/>
    <path d="M60 0 C27 20 27 80 65 100 L100 100 L100 0 Z" fill="url(#photoGlow)"/>
    <path class="visual-arc" d="M60 0 C27 20 27 80 65 100" style="stroke-width:1.5"/>
  </svg>
  <ul class="offer"><li>Unlimited</li><li>PHCE</li><li>CEUs</li><li>$39</li></ul>
  <div class="brand">Medora<span class="brand-dot"></span></div>
</section>

</body>
</html>
```